Sidewalk Sign of store contents

I need a refresh on our current outdoor sandwhich board. We are getting vinyl done up and making a new A- frame sandwhich board. I want vinyl to be all in black with our logo on the top. I find this one attached a bit dated so need a more simple modern design with the logo at the top.

The vinyl will have to have all the words that are on the uploaded file plus the logo at the top. Looking for a nicer more simple modern design.

Oh please do not include the QZMT at the top ...just the circle "Velvet Larder" logo

Hip toronto cocktail lovers

Retail

000000

• Logo at the top. Please check out our website to see our style.
• Must have all the things mentioned on the file I uploaded but with only the "velvet Larder" logo at the top.
• velvetlarderco.com
• This is an outdoor A frame sidewalk sign about 2 feet by 3 feet. It must be eye catching for walkers. Want something more in line with the logo branding.
• It would be nice to have a graphic of a cocktail coupe within the design:)

```html
<!DOCTYPE html>
<html lang="en">
<head>
<meta charset="utf-8">
<title>Velvet Larder – Sidewalk Sign</title>
<link rel="stylesheet" href="https://fonts.googleapis.com/css2?family=Oswald:wght@500;600&display=swap">
<style>
  :root {
    --page-bg: #ffffff;
    --board-bg: #000000;
    --pink: #f6a8c6;
    --peach: #f8c7a6;
    --yellow: #f8e689;
    --rule: #e7d37d;
    --star: #f6d69a;
  }
  html, body {
    margin: 0;
    width: 1200px;
    height: 901px;
    overflow: hidden;
    background: var(--page-bg);
  }
  .sign {
    position: absolute;
    left: 87px;
    top: 50px;
    width: 536px;
    height: 803px;
    background: var(--board-bg);
    font-family: "Oswald", "Arial Narrow", sans-serif;
    font-weight: 500;
    text-transform: uppercase;
    line-height: 1;
  }
  .glow {
    background: linear-gradient(90deg, var(--pink) 0%, var(--peach) 50%, var(--yellow) 100%);
    -webkit-background-clip: text;
    background-clip: text;
    color: transparent;
  }
  .brand {
    position: absolute;
    top: 84px;
    left: 0;
    right: 0;
    text-align: center;
    font-size: 54px;
    text-transform: none;
    color: var(--pink);
  }
  .rule {
    position: absolute;
    left: 55px;
    width: 423px;
    height: 2px;
    background: var(--rule);
  }
  .divider {
    position: absolute;
    left: 298px;
    width: 2px;
    background: var(--rule);
  }
  .line {
    position: absolute;
    left: 55px;
    width: 423px;
    text-align: center;
    white-space: nowrap;
  }
  .cell {
    position: absolute;
    text-align: center;
    white-space: nowrap;
  }
  .left-cell { left: 55px; width: 240px; }
  .right-cell { left: 302px; width: 176px; }

  .categories { top: 220px; font-size: 33px; }
  .bitters-lead { top: 283px; font-size: 23px; }
  .bitters { top: 302px; font-size: 70px; }
  .tiki { top: 270px; font-size: 98px; }
  .glassware, .accessories { top: 400px; font-size: 31px; line-height: 35px; }
  .books { top: 493px; font-size: 61px; }
  .tools { top: 573px; font-size: 94px; }
  .shop { top: 692px; display: flex; justify-content: center; align-items: center; gap: 30px; }
  .shop .label { font-size: 42px; }
  .stars { display: flex; gap: 14px; }
  .stars svg { width: 15px; height: 15px; fill: var(--star); }
  .url { top: 739px; font-size: 24px; }
</style>
</head>
<body>
  <main class="sign">
    <div class="brand">Velvet Larder</div>

    <div class="line categories glow">Garnishes • Syrups • Mixes</div>
    <div class="rule" style="top:261px"></div>

    <div class="cell left-cell bitters-lead glow">Over 200 flavours of</div>
    <div class="cell left-cell bitters glow">Bitters</div>
    <div class="divider" style="top:261px; height:125px"></div>
    <div class="cell right-cell tiki glow">Tiki</div>
    <div class="rule" style="top:386px"></div>

    <div class="cell left-cell glassware glow">New &amp; Vintage<br>Glassware</div>
    <div class="divider" style="top:386px; height:94px"></div>
    <div class="cell right-cell accessories glow">Wine &amp; Beer<br>Accessories</div>
    <div class="rule" style="top:480px"></div>

    <div class="line books glow">Cocktail Books</div>
    <div class="rule" style="top:567px"></div>

    <div class="line tools glow">Bar Tools</div>
    <div class="rule" style="top:679px"></div>

    <div class="line shop">
      <span class="stars" aria-hidden="true">
        <svg viewBox="0 0 24 24"><polygon points="12,1 15,9 23,9 16.5,14 19,22 12,17 5,22 7.5,14 1,9 9,9"/></svg>
        <svg viewBox="0 0 24 24"><polygon points="12,1 15,9 23,9 16.5,14 19,22 12,17 5,22 7.5,14 1,9 9,9"/></svg>
        <svg viewBox="0 0 24 24"><polygon points="12,1 15,9 23,9 16.5,14 19,22 12,17 5,22 7.5,14 1,9 9,9"/></svg>
      </span>
      <span class="label glow">Shop Online</span>
      <span class="stars" aria-hidden="true">
        <svg viewBox="0 0 24 24"><polygon points="12,1 15,9 23,9 16.5,14 19,22 12,17 5,22 7.5,14 1,9 9,9"/></svg>
        <svg viewBox="0 0 24 24"><polygon points="12,1 15,9 23,9 16.5,14 19,22 12,17 5,22 7.5,14 1,9 9,9"/></svg>
        <svg viewBox="0 0 24 24"><polygon points="12,1 15,9 23,9 16.5,14 19,22 12,17 5,22 7.5,14 1,9 9,9"/></svg>
      </span>
    </div>
    <div class="line url glow">velvetlarderco.com</div>
  </main>
</body>
</html>
```